Derek Folsom Resume

Need to update resume with latest position and ensure it stays to 2 pages, may need advice on what to get rid of and simply clean it up, already have a format that i like but am open to change but don't want to spend a fortune

```html
<!DOCTYPE html>
<html lang="en">
<head>
<meta charset="utf-8">
<title>Derek Folsom Resume</title>
<link href="https://fonts.googleapis.com/css2?family=Raleway:wght@200;300;400;600&family=Open+Sans:wght@400;600;700&display=swap" rel="stylesheet">
<style>
:root{
  --ink:#111111;
  --body:#222222;
  --paper:#ffffff;
}
*{margin:0;padding:0;box-sizing:border-box}
html,body{width:848px;height:1200px;overflow:hidden;background:var(--paper)}
.resume{position:relative;width:848px;height:1200px;padding:0 56px 0 54px;color:var(--body);font-family:"Open Sans",Arial,sans-serif;font-size:11.4px;line-height:1.42}
.masthead{text-align:right;padding-top:40px}
.masthead-name{font-family:"Raleway",Arial,sans-serif;font-weight:200;font-size:68px;letter-spacing:0;line-height:1;color:var(--ink);white-space:nowrap;display:inline-block;transform:scaleX(.68);transform-origin:right center;margin-right:6px}
.masthead-rule{width:438px;height:1px;background:var(--ink);margin:4px 0 0 auto}
.masthead-title{font-family:"Raleway",Arial,sans-serif;font-weight:300;font-size:17px;letter-spacing:.6px;color:var(--ink);margin-top:1px;padding-right:2px}
.masthead-contact{font-size:14px;color:var(--ink);margin-top:3px;margin-right:-6px;white-space:nowrap}
.tagline{font-weight:700;font-size:12.6px;color:var(--ink);margin-top:12px}
.summary{font-size:12.8px;margin-top:9px;line-height:1.5}
.highlights{list-style:none;margin:10px 0 0 52px;font-size:12.4px;line-height:1.55}
.highlights li::before{content:"·"}
.section-title{font-family:"Raleway",Arial,sans-serif;font-weight:400;font-size:20.5px;color:var(--ink);text-decoration:underline;text-decoration-thickness:1px;text-underline-offset:3px;letter-spacing:.2px}
.section-title.competencies{margin-top:22px}
.section-title.career{font-weight:600;margin-top:12px}
.competency-list{font-size:12.2px;line-height:1.68;margin-top:6px;color:var(--ink)}
.role{margin-top:8px}
.role-employer{font-family:"Raleway",Arial,sans-serif;font-weight:300;font-size:19px;color:var(--ink);line-height:1.2}
.role-title{font-weight:700;font-size:11px;color:var(--ink);text-transform:uppercase;letter-spacing:.1px}
.role-scope{font-size:11.2px;margin-top:14px;line-height:1.5}
.role-win{text-align:center;font-weight:700;font-size:12px;text-decoration:underline;color:var(--ink);margin-top:12px}
.role-points{margin:10px 0 0 18px;font-size:11.6px;line-height:1.45}
.role-points p{margin:0}
.role-points strong{font-weight:700;color:var(--ink)}
</style>
</head>
<body>
<main class="resume">
  <header class="masthead">
    <h1 class="masthead-name">DEREK W. FOLSOM</h1>
    <div class="masthead-rule"></div>
    <p class="masthead-title">AWARD-WINNING SALES MANAGER</p>
    <p class="masthead-contact">A:1570 Larkspur Court Richmond, VA 23230&nbsp; P:555.240.7731&nbsp; E:derekfolsom@mailbox.com</p>
  </header>

  <p class="tagline">Driving exceptional levels of sales results in competitive industries and changing environments</p>
  <p class="summary">Aggressive, loyal, energetic sales leader with a history of turning around underperforming teams, departments, and territories. Proven consultative sales approach with a focus on product knowledge, trust, and superior service. Strong interpersonal, communication, presentation, and analytical skills.</p>
  <ul class="highlights">
    <li>Developed effective sales incentives and initiatives that became company-wide best practices.</li>
    <li>Drove revenue growth at direct, indirect, and retail sales levels; won multiple prestigious awards.</li>
    <li>Recruited, developed, trained, and motivated high-energy sales/customer support teams.</li>
  </ul>

  <h2 class="section-title competencies">CORE COMPETENCIES INCLUDE:</h2>
  <p class="competency-list">·New Business Development · C-Level Relationship Building · Complex Solution Selling ·<br>High-Impact Sales Presentations · B2C &amp; B2B Channels · Machine to Machine Technology ·<br>Channel Manager ·Performance Management · Competitive Analysis · Salesdesk·Territory Sales Management<br>·SaaS · Budgeting &amp; Forecasting · Vendor Management</p>

  <h2 class="section-title career">CAREER HISTORY</h2>

  <section class="role">
    <p class="role-employer">Veritel April 2016- Present</p>
    <p class="role-title">Regional Sales and Marketing Manager: Mid Atlantic</p>
    <p class="role-scope">Lead a team of sales managers and vendor partners responsible for driving Veritel FiberLink sales and revenue growth in over 200 Big Box locations throughout Virginia, Maryland, DC, New Jersey, Delaware, and Pennsylvania.</p>
    <p class="role-win">Top Performer - #1 RSM in the country in 4Q 2016 and Q1 2017 based on quota performance and revenue growth</p>
    <div class="role-points">
      <p><strong>Retailer Partnerships:</strong> Negotiated a 1st time no cost self service Veritel kiosk inside the #1 retailer in the world resulting in a 200% increase in FiberLink sales</p>
      <p><strong>Set strategy and determine implementation plan</strong> to penetrate Veritel opportunity in the National Big Box retailer channel. Lead and support the business partner relationship to ignite growth and optimize our customer experience</p>
      <p style="margin-top:4px"><strong>Business Development:</strong> Q2 Successfully negotiated and launched FiberLink in Tarvest as a new partner</p>
    </div>
  </section>

  <section class="role">
    <p class="role-employer">Tessaro&nbsp; 2014 – Present</p>
    <p class="role-title">Developmental Executive</p>
    <p class="role-scope">Sell wireless portfolio to the Department of Defense, Department of Homeland Security, Department of Justice, Brandt Ellis Group, and Aerowing</p>
    <p class="role-win">Increased overall revenue in assigned agencies 101.8% YOY.</p>
    <div class="role-points">
      <p><strong>Wireless Solutions:</strong> Facilitate critical communications for U.S. federal government through wireless solutions for networks, infrastructures, and security and surveillance.</p>
      <p><strong>Government Contracts:</strong> Navigate complex matrix of budgeting, bidding, and procurement for government contracts.</p>
      <p><strong>Collaboration:</strong> Work closely with solution engineers, project managers, and C-level executives on identifying the best solutions for their organizations.</p>
    </div>
  </section>

  <section class="role">
    <p class="role-employer">Amtel&nbsp; 2014</p>
    <p class="role-title">Client Business Manager</p>
    <p class="role-scope">Held national responsibility for sales of the entire Amtel solutions portfolio to the Central Treasury. Solutions included mobility, professional services, IP, Cloud, SaaS, Network Infrastructure, and Managed Solutions.</p>
    <p class="role-win">Sold nationwide managed Wi-Fi solution for all 12 Central Treasury Bank locations.</p>
    <div class="role-points">
      <p>Complex Negotiations: Renewed three major contracts resulting in annual revenue of $12 million dollars.</p>
      <p>Partner Relationships: Worked closely with system integrators, distributors, and value-added resellers.</p>
      <p>Strategic Planning: Created strong nationwide strategic sales programs targeted to the Central Treasury.</p>
    </div>
  </section>
</main>
</body>
</html>
```